Retirement maintenance and reinstatment brochure

We are looking for a capability statement/brochure outlining our skills and capabilities for maintenance, reinstatement and refurbishment work specific to the requirements of retirement villages in Australia

We are a new company, however our people have significant experience working in this industry

Target Market(s)

Retirement living facilities, aged care facilities, hospitals

Industry/Entity Type

Building

Colors

Designer to choose colors to be used in the design.

Requirements
Must have
• Not alot of wording. Stock images of building refurbishment to retirement living and aged care (carpenters, painters etc)
Nice to have
• 1-2 pages only
Should not have
• alot of meaningless writing

```html
<!DOCTYPE html>
<html lang="en">
<head>
<meta charset="utf-8">
<title>Swift Reach Maintenance Solutions – Flyer</title>
<link rel="stylesheet" href="https://fonts.googleapis.com/css2?family=Bebas+Neue&family=Arimo:wght@400;700&display=swap">
<style>
  :root {
    --navy: #16497a;
    --navy-dark: #123f6b;
    --red: #cf0a24;
    --white: #ffffff;
    --ink: #1c1c1c;
    --grey-ring: #e4e6ea;
    --page-bg: #e9e9e9;
  }
  * { margin: 0; padding: 0; box-sizing: border-box; }
  html, body { width: 960px; height: 1200px; overflow: hidden; background: var(--page-bg); }
  .flyer {
    position: absolute; left: 16px; top: 0;
    width: 900px; height: 1164px;
    transform: scale(1.0309); transform-origin: top left;
    background: var(--white);
    font-family: "Arimo", Arial, sans-serif;
    overflow: hidden;
  }
  .side-panel { position: absolute; left: 548px; top: 0; width: 352px; height: 1164px; background: var(--navy); }
  .graphics { position: absolute; inset: 0; }
  .display { font-family: "Bebas Neue", "Oswald", sans-serif; font-weight: 400; line-height: 1; }
  .brand { position: absolute; left: 34px; top: 48px; display: flex; align-items: center; gap: 16px; color: var(--navy); }
  .brand-dot { width: 86px; height: 86px; border-radius: 50%; background: var(--navy); }
  .brand-name { font-size: 54px; }
  .brand-sub { font-size: 22px; letter-spacing: 2px; margin-top: 4px; }
  .call { position: absolute; left: 584px; top: 68px; width: 300px; color: var(--white); white-space: nowrap; }
  .call-number { font-size: 46px; letter-spacing: 0.3px; }
  .call-web { font-size: 23px; margin-top: 6px; }
  .headline { position: absolute; left: 100px; top: 506px; font-size: 39px; color: var(--navy); white-space: nowrap; }
  .headline .accent { color: var(--red); display: block; margin-top: 4px; }
  .intro { position: absolute; left: 43px; top: 741px; width: 469px; font-size: 14.2px; line-height: 21px; color: var(--ink); text-align: justify; }
  .promise { position: absolute; left: 43px; top: 880px; width: 470px; font-size: 23px; line-height: 30px; font-weight: 700; color: var(--red); }
  .contact-title { position: absolute; left: 43px; top: 1012px; font-size: 40px; color: var(--navy); }
  .contact-list { position: absolute; left: 43px; top: 1074px; color: var(--navy); font-size: 19px; list-style: none; }
  .contact-list li { display: inline-flex; align-items: center; gap: 8px; height: 30px; }
  .contact-list .email { margin-left: 48px; }
  .contact-list .address { display: flex; }
  .icon { width: 20px; height: 20px; flex: none; }
  .services-title { position: absolute; left: 583px; top: 672px; font-size: 44px; color: var(--white); }
  .services { position: absolute; left: 583px; top: 734px; list-style: none; color: var(--white); font-size: 18px; }
  .services li { display: flex; align-items: center; gap: 10px; height: 33.4px; }
  .tick { width: 19px; height: 19px; flex: none; }
  .credentials { position: absolute; left: 585px; top: 1018px; width: 290px; font-size: 19px; line-height: 24px; font-weight: 700; color: var(--white); }
</style>
</head>
<body>
<main class="flyer">
  <div class="side-panel"></div>

  <svg class="graphics" width="900" height="1164" viewBox="0 0 900 1164">
    <defs>
      <linearGradient id="painterTone" x1="0" y1="0" x2="1" y2="1">
        <stop offset="0" stop-color="#f1f0ee"/><stop offset="0.55" stop-color="#d9d6d2"/><stop offset="1" stop-color="#5c6f93"/>
      </linearGradient>
      <linearGradient id="carpenterTone" x1="0" y1="0" x2="1" y2="1">
        <stop offset="0" stop-color="#e8dccb"/><stop offset="0.6" stop-color="#d8b98e"/><stop offset="1" stop-color="#b98f60"/>
      </linearGradient>
      <linearGradient id="plumberTone" x1="0" y1="0" x2="1" y2="1">
        <stop offset="0" stop-color="#f3f3f3"/><stop offset="0.5" stop-color="#d9cfc8"/><stop offset="1" stop-color="#c8623a"/>
      </linearGradient>
      <linearGradient id="bandTone" x1="0" x2="1">
        <stop offset="0" stop-color="#16497a" stop-opacity="0"/><stop offset="1" stop-color="#b9c6dc"/>
      </linearGradient>
    </defs>

    <rect x="548" y="520" width="160" height="80" fill="url(#bandTone)"/>

    <circle cx="302" cy="430" r="280" fill="none" stroke="var(--grey-ring)" stroke-width="4"/>
    <circle cx="302" cy="430" r="255" fill="var(--navy)"/>
    <g role="img" aria-label="Photo of a painter in a hard hat rolling paint onto a ceiling">
      <circle cx="302" cy="430" r="205" fill="url(#painterTone)"/>
    </g>
    <rect x="80" y="493" width="468" height="107" fill="var(--white)"/>

    <circle cx="598" cy="384" r="176" fill="var(--white)"/>
    <circle cx="598" cy="384" r="164" fill="var(--red)"/>
    <g role="img" aria-label="Photo of a carpenter measuring timber with a tape measure">
      <circle cx="598" cy="384" r="129" fill="url(#carpenterTone)"/>
    </g>

    <circle cx="768" cy="518" r="115" fill="var(--white)"/>
    <circle cx="768" cy="518" r="105" fill="var(--navy)"/>
    <g role="img" aria-label="Photo of a plumber tightening a pipe fitting with a wrench">
      <circle cx="768" cy="518" r="84" fill="url(#plumberTone)"/>
    </g>
  </svg>

  <header class="brand">
    <span class="brand-dot"></span>
    <div>
      <div class="brand-name display">Swift Reach</div>
      <div class="brand-sub display">Maintenance Solutions</div>
    </div>
  </header>

  <div class="call">
    <div class="call-number display">Call: 400 555 019</div>
    <div class="call-web">www.swiftreach.com.au</div>
  </div>

  <h1 class="headline display">The solution for all your <span class="accent">building and maintenance needs</span></h1>

  <p class="intro">We have expertise in retirement living and aged care maintenance works such as cleaning and painting programs, reinstatement works including painting and carpet replacement as well as major refurbishment or upgrade works including kitchen and bathroom works, electrical and air conditioning upgrade works.</p>

  <p class="promise">We have the ability to react quickly and complete works with as little as 24 hours notice.</p>

  <h2 class="contact-title display">Contact us today!</h2>
  <ul class="contact-list">
    <li>
      <svg class="icon" viewBox="0 0 20 20"><circle cx="10" cy="10" r="8.5" fill="none" stroke="var(--red)" stroke-width="1.5"/><path d="M7 5.5l1.6 1.8-1 1.3c.7 1.5 1.7 2.5 3.2 3.2l1.3-1 1.8 1.6-.9 1.6c-3.4-.3-6.6-3.5-6.9-6.9z" fill="var(--red)"/></svg>
      400 555 019
    </li>
    <li class="email">
      <svg class="icon" viewBox="0 0 20 20"><rect x="1.5" y="4" width="17" height="12" fill="none" stroke="var(--red)" stroke-width="1.5"/><path d="M1.5 4l8.5 7 8.5-7M1.5 16l6-5.5M18.5 16l-6-5.5" fill="none" stroke="var(--red)" stroke-width="1.3"/></svg>
      info@swiftreach.com.au
    </li>
    <li class="address">
      <svg class="icon" viewBox="0 0 20 20"><path d="M10 18.5s-6-6.2-6-10.5a6 6 0 0 1 12 0c0 4.3-6 10.5-6 10.5z" fill="none" stroke="var(--red)" stroke-width="1.5"/><circle cx="10" cy="8" r="2.2" fill="none" stroke="var(--red)" stroke-width="1.5"/></svg>
      Hillbrook, Queensland 4500 Australia
    </li>
  </ul>

  <h2 class="services-title display">We specialise in:</h2>
  <ul class="services">
    <li><svg class="tick" viewBox="0 0 20 20"><rect x="1" y="4" width="14" height="14" fill="none" stroke="var(--white)" stroke-width="1.6"/><path d="M4.5 10.5l3.5 4 9-13" fill="none" stroke="var(--white)" stroke-width="2"/></svg>Painting and building cleaning</li>
    <li><svg class="tick" viewBox="0 0 20 20"><rect x="1" y="4" width="14" height="14" fill="none" stroke="var(--white)" stroke-width="1.6"/><path d="M4.5 10.5l3.5 4 9-13" fill="none" stroke="var(--white)" stroke-width="2"/></svg>Carpentry and minor repairs</li>
    <li><svg class="tick" viewBox="0 0 20 20"><rect x="1" y="4" width="14" height="14" fill="none" stroke="var(--white)" stroke-width="1.6"/><path d="M4.5 10.5l3.5 4 9-13" fill="none" stroke="var(--white)" stroke-width="2"/></svg>Plastering and rendering</li>
    <li><svg class="tick" viewBox="0 0 20 20"><rect x="1" y="4" width="14" height="14" fill="none" stroke="var(--white)" stroke-width="1.6"/><path d="M4.5 10.5l3.5 4 9-13" fill="none" stroke="var(--white)" stroke-width="2"/></svg>Carpet and floor laying</li>
    <li><svg class="tick" viewBox="0 0 20 20"><rect x="1" y="4" width="14" height="14" fill="none" stroke="var(--white)" stroke-width="1.6"/><path d="M4.5 10.5l3.5 4 9-13" fill="none" stroke="var(--white)" stroke-width="2"/></svg>Electrical</li>
    <li><svg class="tick" viewBox="0 0 20 20"><rect x="1" y="4" width="14" height="14" fill="none" stroke="var(--white)" stroke-width="1.6"/><path d="M4.5 10.5l3.5 4 9-13" fill="none" stroke="var(--white)" stroke-width="2"/></svg>Plumbing</li>
    <li><svg class="tick" viewBox="0 0 20 20"><rect x="1" y="4" width="14" height="14" fill="none" stroke="var(--white)" stroke-width="1.6"/><path d="M4.5 10.5l3.5 4 9-13" fill="none" stroke="var(--white)" stroke-width="2"/></svg>Air conditioning upgrades</li>
  </ul>

  <p class="credentials">We are licensed and insured, and have a full workplace health and safety compliance system.</p>
</main>
</body>
</html>
```